Tellwick Asset Management - Corporate Letter Head Project

Looking for a classy design based on our current logo. Please find current logo source file in files. With our color scheme.

Target Market(s)

We're an investment firm, the letterhead needs to look professional and attractive to clients.

Industry/Entity Type

Hedgefund

Colors
0054AA
0677BA
7BADD7
CADEEF
E8F1F8

Requirements
Must have
• Our logo, address, phone number, and email

```html
<!DOCTYPE html>
<html lang="en">
<head>
<meta charset="utf-8">
<title>Tellwick Asset Management Letterhead</title>
<link href="https://fonts.googleapis.com/css2?family=Lato:wght@400;700&family=Italianno&display=swap" rel="stylesheet">
<style>
  :root {
    --backdrop: #e3e3e3;
    --paper: #ffffff;
    --paper-edge: #efefef;
    --navy: #1b2a4e;
    --grey-band: #7a7a7a;
    --ink: #3a3a3a;
    --ink-dark: #222222;
  }
  html, body {
    margin: 0;
    width: 1153px;
    height: 1200px;
    overflow: hidden;
    background: var(--backdrop);
  }
  .letterhead {
    position: absolute;
    left: 250px;
    top: 142px;
    width: 654px;
    height: 915px;
    background: radial-gradient(circle at 50% 30%, var(--paper) 0%, #fbfbfb 40%, var(--paper-edge) 100%);
    box-shadow: 0 6px 24px rgba(0,0,0,0.18);
    overflow: hidden;
    font-family: "Lato", sans-serif;
    color: var(--ink);
  }
  .brand {
    position: absolute;
    left: 48px;
    top: 52px;
    display: flex;
    align-items: center;
    gap: 12px;
  }
  .brand-mark {
    width: 48px;
    height: 48px;
    border: 1.5px solid var(--navy);
    box-sizing: border-box;
  }
  .brand-name {
    font-family: "Lato", sans-serif;
    font-weight: 400;
    font-size: 21px;
    color: var(--navy);
    letter-spacing: 0.5px;
    white-space: nowrap;
  }
  .contact {
    position: absolute;
    left: 443px;
    top: 45px;
    height: 76px;
    border-left: 1.2px solid var(--ink-dark);
    padding-left: 10px;
    font-size: 11px;
    color: var(--ink-dark);
    line-height: 14px;
  }
  .contact-address { margin: 2px 0 6px; }
  .contact-line {
    display: flex;
    align-items: center;
    gap: 9px;
    height: 15.5px;
  }
  .contact-line svg { width: 11px; height: 11px; fill: var(--ink-dark); }
  .letter-body {
    position: absolute;
    left: 50px;
    top: 236px;
    width: 553px;
    font-size: 12px;
    line-height: 14.5px;
  }
  .letter-body p { margin: 0; }
  .date { font-size: 13px; margin-bottom: 16px !important; }
  .recipient { margin-bottom: 15px !important; line-height: 15px !important; }
  .recipient-company { margin-bottom: 18px !important; line-height: 15px !important; }
  .salutation {
    font-size: 15px;
    font-weight: 700;
    color: var(--ink-dark);
    margin-bottom: 14px !important;
  }
  .paragraph {
    text-align: justify;
    margin-bottom: 14px !important;
  }
  .closing { margin-top: 30px !important; }
  .signature {
    font-family: "Italianno", cursive;
    font-size: 38px;
    color: var(--ink-dark);
    margin-top: 12px !important;
    margin-left: 3px !important;
  }
  .footer-waves {
    position: absolute;
    left: 0;
    bottom: 0;
    width: 654px;
    height: 80px;
  }
</style>
</head>
<body>
  <main class="letterhead">
    <header>
      <div class="brand">
        <div class="brand-mark"></div>
        <div class="brand-name">Tellwick Asset Management</div>
      </div>
      <address class="contact" style="font-style:normal">
        <p class="contact-address">2480 Harwell Street, Ste<br>300, Fairlow, TX 750392</p>
        <div class="contact-line">
          <svg viewBox="0 0 24 24"><path d="M6.6 10.8a15 15 0 0 0 6.6 6.6l2.2-2.2c.3-.3.7-.4 1-.2 1.1.4 2.3.6 3.6.6.6 0 1 .4 1 1V20c0 .6-.4 1-1 1A17 17 0 0 1 3 4c0-.6.4-1 1-1h3.5c.6 0 1 .4 1 1 0 1.3.2 2.5.6 3.6.1.3 0 .7-.2 1z"/></svg>
          <span>214-630-7718</span>
        </div>
        <div class="contact-line">
          <svg viewBox="0 0 24 24"><path d="M2 5h20v14H2z M2 5l10 7 10-7" stroke="#fff" stroke-width="1.5"/></svg>
          <span>hello@tellwick-mail.com</span>
        </div>
        <div class="contact-line">
          <svg viewBox="0 0 24 24"><circle cx="12" cy="12" r="10"/></svg>
          <span>www.tellwick-web.com</span>
        </div>
      </address>
    </header>

    <section class="letter-body">
      <p class="date">Feb-03-2022</p>
      <p class="recipient">Mr, Peter Lancey<br>President</p>
      <p class="recipient-company">Brightfield Corporation<br>123 Street Name, Suite# 10<br>City, State, 120023</p>
      <p class="salutation">Dear Mr, Peter</p>
      <p class="paragraph">Lorem ipsum dolor sit amet, consectetur adipisicing elit, sed do eiusmod tempor incididunt ut labore et dolore magna aliqua. Ut enim ad minim veniam, quis nostrud exercitation ullamco laboris nisi ut aliquip ex ea commodo consequat. Duis aute irure dolor in reprehenderit in voluptate velit esse cillum dolore eu fugiat nulla pariatur.</p>
      <p class="paragraph">Lorem ipsum dolor sit amet, consectetur adipisicing elit, sed do eiusmod tempor incididunt ut labore et dolore magna aliqua. Ut enim ad minim veniam, quis nostrud exercitation ullamco laboris nisi ut aliquip ex ea commodo consequat. Duis aute irure dolor in reprehenderit in voluptate velit esse cillum dolore eu fugiat nulla pariatur.</p>
      <p class="paragraph">Lorem ipsum dolor sit amet, consectetur adipisicing elit, sed do eiusmod tempor incididunt ut labore et dolore magna aliqua. Ut enim ad minim veniam, quis nostrud exercitation ullamco laboris nisi ut aliquip ex ea commodo consequat.</p>
      <p class="paragraph">Excepteur sint occaecat cupidatat non proident, sunt in culpa qui officia deserunt mollit anim id est laborum. re et dolore magnam aliquam quaerat voluptatem.</p>
      <p class="closing">Regards</p>
      <p class="signature">Daniel Harrow</p>
    </section>

    <svg class="footer-waves" viewBox="0 0 654 80" preserveAspectRatio="none" aria-hidden="true">
      <path d="M0,72 Q327,-45 654,54 L654,58 Q327,7 0,76 Z" fill="var(--grey-band)"/>
      <path d="M0,66 Q327,-14.5 654,63 L654,80 L0,80 Z" fill="var(--navy)"/>
    </svg>
  </main>
</body>
</html>
```